Biz cards

Need some business cards to handout when finding clients for medical marijuana

Industry/Entity Type

Business

Contact Information for Business Card

Name: Tobin Velk
Cell #555-314-2297
Instagram: lunarharvestco

Requirements
Must have
• Needs to say ( on back of card with my info )
• MMAR Producer
• Marijuana Enthusiest and connoisseur

```html
<!DOCTYPE html>
<html lang="en">
<head>
<meta charset="utf-8">
<title>Lunar Harvest – Business Cards</title>
<link rel="stylesheet" href="https://fonts.googleapis.com/css2?family=Montserrat:wght@400;700;800&display=swap">
<style>
  :root {
    --bg: #d9d4cc;
    --card-white: #ffffff;
    --ink: #111111;
    --brand-red: #e8232a;
    --back-black: #000000;
    --leaf-dark: #1d3a1f;
    --leaf-mid: #4f7a45;
    --line-grey: #d6d6d6;
  }
  * { margin: 0; padding: 0; box-sizing: border-box; }
  html, body { width: 900px; height: 1200px; overflow: hidden; }
  body {
    background: var(--bg);
    font-family: "Montserrat", sans-serif;
    position: relative;
  }
  .card {
    position: absolute;
    left: 83px;
    width: 734px;
    height: 429px;
    box-shadow: 0 4px 12px rgba(0,0,0,0.25);
  }
  .card-front { top: 131px; background: var(--card-white); overflow: hidden; }
  .card-front .frame { position: absolute; inset: 0; }

  .brand {
    position: absolute;
    left: 44px;
    top: 52px;
    display: flex;
    flex-direction: column;
    align-items: flex-start;
  }
  .brand-dot {
    width: 46px; height: 46px;
    border-radius: 50%;
    background: var(--brand-red);
    margin: 0 0 12px 64px;
  }
  .brand-name {
    font-weight: 800;
    font-size: 38px;
    line-height: 1.02;
    color: var(--ink);
    letter-spacing: 0.5px;
  }

  .holder { position: absolute; left: 44px; top: 244px; width: 280px; }
  .holder-name { font-weight: 800; font-size: 22px; color: var(--ink); letter-spacing: 0.5px; }
  .holder-role { font-size: 14.5px; color: var(--brand-red); line-height: 1.4; margin-top: 4px; }
  .holder-rule { height: 1px; background: var(--brand-red); opacity: 0.6; margin-top: 8px; width: 279px; }

  .contact { list-style: none; margin-top: 12px; }
  .contact li {
    display: flex; align-items: center; gap: 9px;
    font-size: 14.5px; color: var(--ink); height: 23px;
  }
  .contact-icon {
    width: 20px; height: 20px; border-radius: 50%;
    background: var(--brand-red);
    display: flex; align-items: center; justify-content: center;
  }

  .card-back {
    top: 640px;
    background: var(--back-black);
    border: 26px solid var(--brand-red);
    display: flex; flex-direction: column; align-items: center; justify-content: center;
  }
  .card-back .brand-dot { background: #ffffff; margin: 0 0 12px 0; }
  .card-back .brand-name { color: #ffffff; text-align: center; font-size: 34px; }
</style>
</head>
<body>

<section class="card card-front">
  <svg class="frame" width="734" height="429" viewBox="0 0 734 429">
    <defs>
      <radialGradient id="foliage" cx="55%" cy="40%" r="70%">
        <stop offset="0" stop-color="var(--leaf-mid)"/>
        <stop offset="0.6" stop-color="#2e5230"/>
        <stop offset="1" stop-color="var(--leaf-dark)"/>
      </radialGradient>
    </defs>
    <polyline points="170,0 330,92" fill="none" stroke="var(--ink)" stroke-width="2"/>
    <polyline points="565,0 734,95" fill="none" stroke="var(--ink)" stroke-width="2"/>
    <polyline points="185,429 335,345 480,429" fill="none" stroke="var(--ink)" stroke-width="2"/>
    <polygon points="734,340 734,429 572,429" fill="var(--brand-red)"/>
    <polygon role="img" aria-label="Close-up photo of a flowering cannabis plant"
      points="344,112 415,5 640,5 714,112 714,330 598,429 502,429 344,330"
      fill="url(#foliage)"/>
  </svg>

  <div class="brand">
    <span class="brand-dot"></span>
    <span class="brand-name">LUNAR<br>HARVEST</span>
  </div>

  <div class="holder">
    <h1 class="holder-name">TOBIN VELK</h1>
    <p class="holder-role">MMAR Producer<br>Marijuana Enthusiest and Connoisseur</p>
    <div class="holder-rule"></div>
    <ul class="contact">
      <li>
        <span class="contact-icon">
          <svg width="12" height="12" viewBox="0 0 24 24"><path fill="#fff" d="M6.6 10.8a15.1 15.1 0 0 0 6.6 6.6l2.2-2.2a1 1 0 0 1 1-.25 11.4 11.4 0 0 0 3.6.57 1 1 0 0 1 1 1V20a1 1 0 0 1-1 1A17 17 0 0 1 3 4a1 1 0 0 1 1-1h3.5a1 1 0 0 1 1 1c0 1.25.2 2.45.57 3.57a1 1 0 0 1-.25 1z"/></svg>
        </span>
        555-314-2297
      </li>
      <li>
        <span class="contact-icon"></span>
        lunarharvestco
      </li>
    </ul>
  </div>
</section>

<section class="card card-back">
  <span class="brand-dot"></span>
  <span class="brand-name">LUNAR<br>HARVEST</span>
</section>

</body>
</html>
```